Web Design Project - Homepage mockup for media services company

Client would like a site much like this example below in terms of design and layout:

http://fernquill.net/

It's a media services company and the services they provide are:
-audio/video production
-graphic design
-social media
-web development
-apparel design

Their logo file is attached. I have also attached some of their service descriptions if that at all helps with things.

```html
<!DOCTYPE html>
<html lang="en">
<head>
<meta charset="utf-8">
<title>R. Valdane — Media Services</title>
<link href="https://fonts.googleapis.com/css2?family=Gelasio:wght@400;700&family=Sorts+Mill+Goudy&display=swap" rel="stylesheet">
<style>
  :root{
    --ink:#1e1a1a;
    --maroon:#6e1f22;
    --maroon-dark:#4f1416;
    --panel-red:#8a3638;
    --paper:#ffffff;
    --footer:#3a3a3a;
    --footer-bottom:#232323;
    --link:#3fa9e0;
    --field-top:#c9c9c9;
    --field-bottom:#9b9b9b;
  }
  *{box-sizing:border-box;margin:0;padding:0}
  html,body{width:960px;height:1200px;overflow:hidden}
  body{
    position:relative;
    font-family:"Gelasio",Georgia,serif;
    color:var(--ink);
    background:
      radial-gradient(ellipse 420px 260px at 330px 40px,#f2f2f2 0%,rgba(242,242,242,0) 100%),
      linear-gradient(#d6d6d6 0px,#cfcfcf 160px,#b4b4b4 330px,#a7a7a7 520px,#9c9c9c 935px);
  }
  .abs{position:absolute}

  /* header */
  .brand{left:92px;top:14px;display:flex;align-items:center;gap:12px}
  .brand-mark{width:78px;height:78px;border-radius:50%;background:#2a2626}
  .brand-name{font-family:"Sorts Mill Goudy",serif;font-size:40px;color:#2a2626;line-height:1}
  .call{right:164px;top:34px;font-size:14px;color:#2a2626}
  .call b{font-size:19px;font-weight:400;color:var(--maroon)}
  .social{display:flex;gap:7px}
  .social span{width:24px;height:24px;border-radius:50%;background:#5a5a5a;display:block}
  .social.top{right:92px;top:33px}
  .nav{right:92px;top:81px;display:flex;gap:14px;font-size:15px;text-transform:uppercase}
  .nav a{color:#1e1a1a;text-decoration:none}
  .nav a.current{color:var(--maroon)}
  .nav .caret{font-size:10px;margin-left:2px}

  /* slider */
  .slider{left:95px;top:120px;width:774px;height:335px;display:flex;box-shadow:0 2px 6px rgba(0,0,0,.3)}
  .slide-photo{width:459px;height:100%;
    background:radial-gradient(ellipse 360px 260px at 40% 40%,#eadfc8 0%,#d6c4a4 55%,#a99a86 100%)}
  .slide-info{flex:1;background:var(--panel-red);color:#fff;padding:40px 0 0 27px}
  .slide-info h2{font-family:"Sorts Mill Goudy",serif;font-weight:400;font-size:33px;line-height:29px}
  .slide-info ul{list-style:none;margin-top:17px}
  .slide-info li{font-size:14px;height:28.8px;display:flex;align-items:center;gap:10px}
  .slide-info li svg{width:8px;height:11px}
  .arrow{top:262px;width:32px;height:32px;border-radius:50%;background:#111;display:flex;align-items:center;justify-content:center}
  .arrow.prev{left:80px}.arrow.next{left:848px}

  /* intro */
  .welcome{left:95px;top:474px;width:456px}
  .welcome h1{font-family:"Sorts Mill Goudy",serif;font-weight:400;font-size:33px;color:var(--maroon);letter-spacing:.3px;text-shadow:0 0 .6px var(--maroon)}
  .welcome p{margin-top:8px;font-size:11.2px;line-height:15.2px;text-align:justify}
  .testimonial{left:588px;top:473px;width:282px}
  .testimonial h3{font-family:"Sorts Mill Goudy",serif;font-weight:400;font-size:23px;color:var(--maroon);display:flex;align-items:flex-start;gap:8px;height:34px}
  .testimonial .quote{font-family:Georgia,serif;font-weight:700;font-size:48px;line-height:48px;color:#7e7e7e}
  .testimonial p{margin:12px 0 0 3px;font-size:11.2px;line-height:15.2px;text-align:justify}
  .testimonial cite{display:block;margin-left:3px;font-style:normal;font-size:11.2px;color:var(--maroon)}

  /* services */
  .paper{left:76px;top:630px;width:804px;height:270px}
  .services-title{left:0;width:954px;top:671px;text-align:center;font-size:19.5px;font-weight:400;text-transform:uppercase}
  .service{top:714px;width:150px;text-align:center}
  .service .badge{width:91px;height:91px;border-radius:50%;margin:0 auto;
    background:radial-gradient(circle at 50% 45%,#a5a5a5,#7b7b7b);box-shadow:inset 0 0 0 2px #6d6d6d}
  .service h4{margin-top:23px;font-weight:400;font-size:14.5px;line-height:15.5px;color:var(--maroon-dark);text-transform:uppercase}

  /* footer */
  .footer-band{left:0;top:935px;width:960px;height:200px;background:var(--footer)}
  .footer-bottom{left:0;top:1135px;width:960px;height:65px;background:var(--footer-bottom)}
  .footer-title{font-family:"Sorts Mill Goudy",serif;font-weight:400;font-size:24px;line-height:30px;color:#fff}
  .quote-form{left:87px;top:953px;width:470px;height:170px}
  .field{position:absolute;background:linear-gradient(var(--field-top),var(--field-bottom));border-radius:2px;font-size:11.5px;color:#333;padding:9px 7px}
  .submit{position:absolute;left:3px;top:123px;width:126px;height:37px;background:linear-gradient(#7a1a1d,#4b0e10);color:#fff;font-size:14.5px;display:flex;align-items:center;justify-content:center;border-radius:2px}
  .tweets{left:608px;top:953px;width:262px;color:#fff}
  .tweets .footer-title{display:flex;align-items:center;gap:10px}
  .tweets .footer-title span{width:16px;height:16px;background:var(--link);border-radius:3px;display:block}
  .tweets p{margin:9px 0 0 2px;font-size:11.4px;line-height:14.5px;color:#ececec}
  .tweets p + p{margin-top:14px}
  .tweets a{color:var(--link);text-decoration:none}
  .footer-links{left:88px;top:1149px;display:flex;gap:12px;font-size:12.5px;color:#bdbdbd}
  .copyright{left:88px;top:1169px;font-size:10px;color:#5c5c5c}
  .social.bottom{right:104px;top:1153px}
  .social.bottom span{background:#8a8a8a}
</style>
</head>
<body>

<header>
  <div class="abs brand"><span class="brand-mark"></span><span class="brand-name">R. Valdane</span></div>
  <div class="abs call">Call us at <b>014 555 0192</b></div>
  <div class="abs social top"><span></span><span></span></div>
  <nav class="abs nav">
    <a class="current" href="#">Home</a><a href="#">About us</a><a href="#">Services<span class="caret">&#9660;</span></a><a href="#">Works</a><a href="#">Contact us</a>
  </nav>
</header>

<section class="abs slider">
  <div class="slide-photo" role="img" aria-label="Screenshot of a resort website with a photo of villas beside a pool"></div>
  <div class="slide-info">
    <h2>Web Design and Development Services</h2>
    <ul>
      <li><svg viewBox="0 0 8 11"><path d="M1 1l5 4.5L1 10" stroke="#fff" stroke-width="2" fill="none"/></svg>Web Design and Redesign</li>
      <li><svg viewBox="0 0 8 11"><path d="M1 1l5 4.5L1 10" stroke="#fff" stroke-width="2" fill="none"/></svg>Web Development</li>
      <li><svg viewBox="0 0 8 11"><path d="M1 1l5 4.5L1 10" stroke="#fff" stroke-width="2" fill="none"/></svg>Custom Applications</li>
      <li><svg viewBox="0 0 8 11"><path d="M1 1l5 4.5L1 10" stroke="#fff" stroke-width="2" fill="none"/></svg>Content Management System</li>
      <li><svg viewBox="0 0 8 11"><path d="M1 1l5 4.5L1 10" stroke="#fff" stroke-width="2" fill="none"/></svg>Ecommerce Solutions</li>
      <li><svg viewBox="0 0 8 11"><path d="M1 1l5 4.5L1 10" stroke="#fff" stroke-width="2" fill="none"/></svg>Web Hosting Solutions</li>
    </ul>
  </div>
</section>
<div class="abs arrow prev"><svg width="10" height="14" viewBox="0 0 10 14"><path d="M8 2L3 7l5 5" stroke="#fff" stroke-width="3" fill="none"/></svg></div>
<div class="abs arrow next"><svg width="10" height="14" viewBox="0 0 10 14"><path d="M2 2l5 5-5 5" stroke="#fff" stroke-width="3" fill="none"/></svg></div>

<section class="abs welcome">
  <h1>Welcome to R. Valdane</h1>
  <p>Lorem ipsum dolor sit amet, consectetur adipiscing elit. Sed est turpis, facilisis in pretium lobortis, imperdiet et lectus. Donec et elit mauris. Etiam diam risus, dapibus sed interdum ut, fringilla et turpis. Pellentesque lobortis velit ac quam ornare ultricies. Etiam aliquam vehicula metus, sit amet blandit nunc ornare eget. Etiam a adipiscing augue. Pellentesque consequat sem id lacus fringilla vulputate. Mauris egestas elementum leo, et tincidunt arcu sodales a.</p>
</section>

<aside class="abs testimonial">
  <h3>Client Testimonials <span class="quote">&ldquo;</span></h3>
  <p>Duis congue sollicitudin sem, sed mollis purus cursus sit amet. Sed faucibus velit at libero cursus interdum. Vivamus et libero quis leo accumsan rutrum. Curabitur dolor sem,</p>
  <cite>-Peter Holm</cite>
</aside>

<svg class="abs paper" viewBox="0 0 804 270">
  <path d="M32 17 L784 13 Q790 160 798 263 Q420 255 28 250 Q40 170 32 17Z" fill="#000" opacity=".25" transform="translate(2,6)"/>
  <path d="M32 17 L784 13 Q786 160 798 258 Q420 248 4 245 Q30 165 32 17Z" fill="var(--paper)"/>
  <rect x="350" y="4" width="120" height="30" fill="#f4f4f4" opacity=".85" transform="rotate(-2 410 19)"/>
</svg>
<h2 class="abs services-title">Services We Offer</h2>
<div class="abs service" style="left:108px"><div class="badge" role="img" aria-label="Film reel icon"></div><h4>Audio/Video<br>Production</h4></div>
<div class="abs service" style="left:257px"><div class="badge" role="img" aria-label="Paint palette icon"></div><h4>Graphic<br>Design</h4></div>
<div class="abs service" style="left:405px"><div class="badge" role="img" aria-label="Bird on a perch icon"></div><h4>Social<br>Media</h4></div>
<div class="abs service" style="left:555px"><div class="badge" role="img" aria-label="Globe with magnifier icon"></div><h4>Web<br>Development</h4></div>
<div class="abs service" style="left:704px"><div class="badge" role="img" aria-label="Shirt icon"></div><h4>Apparel<br>Design</h4></div>

<footer>
  <div class="abs footer-band"></div>
  <div class="abs footer-bottom"></div>

  <div class="abs quote-form">
    <h3 class="footer-title">Request a Quote</h3>
    <div class="field" style="left:3px;top:39px;width:228px;height:32px">Your Name</div>
    <div class="field" style="left:3px;top:80px;width:228px;height:32px">Your Email ID</div>
    <div class="field" style="left:240px;top:39px;width:229px;height:73px">Service Required</div>
    <div class="submit">SUBMIT</div>
  </div>

  <div class="abs tweets">
    <h3 class="footer-title">Recent Tweets <span></span></h3>
    <p>Morbi non nunc mauris, pretium malesuada lectus. Ut id ligula id felis accumsan <a href="#">http://lnk.to/QWRTZP 2 days ago</a>.</p>
    <p>Curabitur sed lacus at mi gravida ultrices. In hac habitasse platea dictumst.<br><a href="#">http://lnk.to/MVBNXQLRP 4 days ago</a>.</p>
  </div>

  <div class="abs footer-links"><span>Home</span><span>About us</span><span>Services</span><span>Works</span><span>Contact us</span><span>Testimonials</span><span>Terms &amp; Conditions</span><span>Privacy Policy</span></div>
  <div class="abs copyright">Copyright &copy; R. Valdane. All rights reserved.</div>
  <div class="abs social bottom"><span></span><span></span></div>
</footer>

</body>
</html>
```